New business card design needed for Diesel Fitting (Mechanical) Company

We need a new business card for our company called "Granite Valley Engineering" that showcases our logo and business details.
Target Market(s)
Owners of all makes and models of vehicles, trucks, plant and machinery.
Industry/Entity Type
Mechanical
Contact Information for Business Card
The business card details need to include the following: Owners/Directors: Trevor & Marisol Dunn-Calloway ABN: 47 913 206 781 Address: 561 Beaumont Street CHARTERS TOWERS QLD 4820 Postal Address: PO Box 8716 CHARTERS TOWERS QLD 4820 Website: www.gvengineering.com.au Phone: 4732 9185 Mobile: 0491 375 806 Emails: sales@gvengineering.com.au; admin@gvengineering.com.au; accounts@gvengineering.com.au; parts@gvengineering.com.au; office@gvengineering.com.au, reception@gvengineering.com.au
Look and feel

```html
<!DOCTYPE html>
<html lang="en">
<head>
<meta charset="utf-8">
<title>Granite Valley Engineering – Business Card</title>
<link rel="stylesheet" href="https://fonts.googleapis.com/css2?family=Montserrat:wght@400;500;700&display=swap">
<style>
  :root {
    --red: #e8232a;
    --orange: #f07a22;
    --ink: #1a1a1a;
    --paper: #ffffff;
    --stage: #e9e9e9;
  }
  * { box-sizing: border-box; margin: 0; padding: 0; }
  html, body { width: 1200px; height: 900px; overflow: hidden; }
  body {
    background: var(--stage);
    font-family: "Montserrat", Arial, sans-serif;
    color: var(--ink);
    display: flex;
    flex-direction: column;
    align-items: center;
    justify-content: center;
    gap: 40px;
  }
  .card {
    width: 700px;
    height: 400px;
    position: relative;
    overflow: hidden;
    box-shadow: 0 6px 18px rgba(0,0,0,.18);
  }

  /* Front */
  .card-front {
    background: var(--red);
    display: flex;
    align-items: center;
    justify-content: center;
  }
  .brand {
    display: flex;
    align-items: center;
    gap: 18px;
    font-weight: 500;
  }
  .brand-dot { border-radius: 50%; flex: none; }
  .card-front .brand { color: var(--paper); font-size: 34px; line-height: 1.15; }
  .card-front .brand-dot { width: 70px; height: 70px; background: var(--paper); }

  /* Back */
  .card-back { background: var(--paper); }
  .card-back .brand {
    position: absolute; left: 40px; top: 60px;
    color: var(--ink); font-size: 22px; line-height: 1.2;
  }
  .card-back .brand-dot { width: 46px; height: 46px; background: var(--orange); }

  .owners {
    position: absolute; left: 30px; top: 180px; width: 370px;
    text-align: right;
  }
  .owners-name { color: var(--red); font-weight: 700; font-size: 16px; white-space: nowrap; }
  .owners-role, .owners-abn { font-size: 15px; margin-top: 8px; }

  .divider {
    position: absolute; left: 420px; top: 36px;
    width: 2px; height: 250px; background: var(--red);
  }

  .contacts {
    position: absolute; left: 438px; top: 26px;
    list-style: none;
  }
  .contacts li {
    display: flex; align-items: center; gap: 10px;
    font-size: 13px; height: 26px; white-space: nowrap;
  }
  .contacts svg { width: 16px; height: 16px; flex: none; fill: var(--red); }

  .address-band {
    position: absolute; left: 0; right: 0; top: 300px; height: 40px;
    background: var(--red); color: var(--paper);
    display: flex; align-items: center; padding-left: 40px;
    font-size: 15px; font-weight: 500;
  }
  .postal {
    position: absolute; left: 40px; top: 352px;
    font-size: 15px; font-weight: 500;
  }
</style>
</head>
<body>
  <svg width="0" height="0" style="position:absolute" aria-hidden="true">
    <symbol id="i-phone" viewBox="0 0 24 24"><path d="M6.6 10.8a15.1 15.1 0 0 0 6.6 6.6l2.2-2.2a1 1 0 0 1 1-.25 11.4 11.4 0 0 0 3.6.6 1 1 0 0 1 1 1V20a1 1 0 0 1-1 1A17 17 0 0 1 3 4a1 1 0 0 1 1-1h3.5a1 1 0 0 1 1 1c0 1.25.2 2.450.6 3.6a1 1 0 0 1-.25 1z"/></symbol>
    <symbol id="i-mobile" viewBox="0 0 24 24"><path d="M7 1h10a2 2 0 0 1 2 2v18a2 2 0 0 1-2 2H7a2 2 0 0 1-2-2V3a2 2 0 0 1 2-2zm0 3v15h10V4zm5 16.2a.9.9 0 1 0 0 1.8.9.9 0 0 0 0-1.8z"/></symbol>
    <symbol id="i-mail" viewBox="0 0 24 24"><path d="M2 5h20v14H2zm2 2v.4l8 5.2 8-5.2V7zm0 2.8V17h16V9.8l-8 5.2z"/></symbol>
    <symbol id="i-web" viewBox="0 0 24 24"><path d="M12 2a10 10 0 1 0 0 20 10 10 0 0 0 0-20zm0 2c.9 0 2.2 1.9 2.8 5H9.2C9.8 5.9 11.1 4 12 4zM4.3 11h4.7a20 20 0 0 0 0 2H4.3a8 8 0 0 1 0-2zm10.7 0h4.7a8 8 0 0 1 0 2H15a20 20 0 0 0 0-2zm-4 0h2a18 18 0 0 1 0 2h-2a18 18 0 0 1 0-2zm-1.8 4h5.6c-.6 3.1-1.9 5-2.8 5s-2.2-1.9-2.8-5z"/></symbol>
  </svg>

  <section class="card card-front">
    <div class="brand">
      <span class="brand-dot"></span>
      <span>Granite Valley<br>Engineering</span>
    </div>
  </section>

  <section class="card card-back">
    <div class="brand">
      <span class="brand-dot"></span>
      <span>Granite Valley<br>Engineering</span>
    </div>

    <div class="owners">
      <p class="owners-name">TREVOR &amp; MARISOL DUNN-CALLOWAY</p>
      <p class="owners-role">Owners/Directors</p>
      <p class="owners-abn">ABN: 47 913 206 781</p>
    </div>

    <div class="divider"></div>

    <ul class="contacts">
      <li><svg><use href="#i-phone"/></svg>4732 9185</li>
      <li><svg><use href="#i-mobile"/></svg>0491 375 806</li>
      <li><svg><use href="#i-mail"/></svg>sales@gvengineering.com.au</li>
      <li><svg><use href="#i-mail"/></svg>admin@gvengineering.com.au</li>
      <li><svg><use href="#i-mail"/></svg>accounts@gvengineering.com.au</li>
      <li><svg><use href="#i-mail"/></svg>parts@gvengineering.com.au</li>
      <li><svg><use href="#i-mail"/></svg>office@gvengineering.com.au</li>
      <li><svg><use href="#i-mail"/></svg>reception@gvengineering.com.au</li>
      <li><svg><use href="#i-web"/></svg>www.gvengineering.com.au</li>
    </ul>

    <div class="address-band">561 Beaumont Street CHARTERS TOWERS QLD 4820 Postal</div>
    <p class="postal">PO Box 8716 CHARTERS TOWERS QLD 4820</p>
  </section>
</body>
</html>
```